Standard Company Posters / Notices

We have manufacturing sites, across the sites there are notices that managers put up, sometimes like a poster or door notice. These are not in any standard format or follow any standard layout. We wanted to create a notice template that could be adopted with layout guidance for all our internal notices. Some examples of the notices are below. We have three different sites so we would want to interchange the logo to suit the location, I have also added some images used for our values awards as examples of the look we like.

Target Market(s)

Employees

Industry/Entity Type

Food Manufacturing

Requirements
Must have
• Flexible for the site teams to amend to suit their needs.

```html
<!DOCTYPE html>
<html lang="en">
<head>
<meta charset="utf-8">
<title>Site Notice Templates</title>
<link href="https://fonts.googleapis.com/css2?family=Montserrat:wght@400;500;600;700;800;900&display=swap" rel="stylesheet">
<style>
  :root{
    --navy:#00216a;
    --navy-deep:#0d2270;
    --red:#c8102e;
    --frame-blue:#b3bacb;
    --frame-grey:#d6d6d6;
    --head-grey:#d6d6d6;
    --ink:#111111;
    --grey-ink:#666666;
    --grey-bar:#666666;
    --paper:#ffffff;
  }
  html,body{margin:0;padding:0;overflow:hidden;}
  body{width:1200px;height:993px;background:var(--navy);font-family:"Montserrat",sans-serif;}
  .board{position:absolute;left:0;top:0;width:2100px;height:1738px;transform:scale(0.5714);transform-origin:0 0;}
  .notice{position:absolute;width:425px;height:608px;background:var(--paper);}
  .frame{position:absolute;left:22px;top:18px;width:381px;height:572px;border-radius:40px;padding:14px;box-sizing:border-box;background:var(--frame-blue);}
  .notice--mono .frame{background:var(--frame-grey);}
  .panel{height:100%;box-sizing:border-box;border:7px solid var(--navy-deep);border-radius:28px;background:var(--paper);overflow:hidden;display:flex;flex-direction:column;}
  .notice--mono .panel{border-color:#111;}
  .panel-head{height:120px;flex:none;background:var(--red);color:#fff;text-align:center;display:flex;flex-direction:column;justify-content:center;}
  .notice--mono .panel-head{background:var(--head-grey);color:#111;}
  .head-main{font-weight:900;font-size:50px;line-height:46px;letter-spacing:1px;}
  .head-sub{font-weight:800;font-size:42px;line-height:42px;}
  .panel-body{flex:1;display:flex;flex-direction:column;align-items:center;text-align:center;color:var(--ink);padding:0 20px 34px;}
  .notice--mono .panel-body{color:var(--grey-ink);}
  .accent{color:var(--red);}
  .notice--mono .accent{color:var(--grey-ink);}
  .line{font-weight:700;font-size:22px;line-height:25px;}
  .big{font-weight:800;font-size:46px;line-height:46px;}
  .title{font-weight:800;font-size:37px;line-height:38px;}
  .title-sub{font-weight:700;font-size:29px;line-height:32px;}
  .pill{background:linear-gradient(90deg,var(--red) 20%,var(--navy-deep));color:#fff;font-weight:700;border-radius:4px;}
  .notice--mono .pill{background:var(--grey-bar);}
  .pill--note{font-size:22px;line-height:25px;padding:2px 20px;margin-top:20px;}
  .kit{list-style:none;margin:12px 0 0;padding:0;width:283px;}
  .kit li{font-size:20px;line-height:27px;margin-bottom:9px;}
  .copy{font-weight:400;font-size:17px;line-height:20px;margin:0 0 14px;}
  .copy strong{font-weight:700;}
  .pill--credit{font-size:13.5px;line-height:22px;padding:0 6px;font-weight:600;}
  .brand{margin-top:auto;font-weight:800;font-size:26px;letter-spacing:1px;color:var(--red);display:flex;align-items:center;gap:10px;}
  .brand-mark{width:16px;height:16px;background:var(--navy-deep);}
  .notice--mono .brand{color:#6b6b6b;}
  .notice--mono .brand-mark{background:#6b6b6b;}
</style>
</head>
<body>
<div class="board">

  <!-- Row 1 -->
  <section class="notice" style="left:155px;top:245px">
    <div class="frame"><div class="panel">
      <header class="panel-head"><div class="head-main">ATTENTION</div><div class="head-sub">PLEASE!</div></header>
      <div class="panel-body" style="padding-top:50px">
        <div class="line">MOBILE PHONES ARE</div>
        <div class="big accent">PROHIBITED</div>
        <div class="line">IN THIS AREA<br>UNLESS YOU ARE</div>
        <div class="big accent">AUTHORISED</div>
        <div class="line">AND ON THE<br>CONCESSION LIST!</div>
        <div class="brand"><span class="brand-mark"></span>MARLOW DALE</div>
      </div>
    </div></div>
  </section>

  <section class="notice notice--mono" style="left:610px;top:245px">
    <div class="frame"><div class="panel">
      <header class="panel-head"><div class="head-main">ATTENTION</div><div class="head-sub">PLEASE!</div></header>
      <div class="panel-body" style="padding-top:50px">
        <div class="line">MOBILE PHONES ARE</div>
        <div class="big accent">PROHIBITED</div>
        <div class="line">IN THIS AREA<br>UNLESS YOU ARE</div>
        <div class="big accent">AUTHORISED</div>
        <div class="line">AND ON THE<br>CONCESSION LIST!</div>
        <div class="brand">BRENWICK FOODS</div>
      </div>
    </div></div>
  </section>

  <section class="notice" style="left:1065px;top:245px">
    <div class="frame"><div class="panel">
      <header class="panel-head"><div class="head-main">ATTENTION</div><div class="head-sub">PLEASE!</div></header>
      <div class="panel-body" style="padding-top:28px">
        <div class="title accent">FEMALE<br>VISITORS</div>
        <div class="title-sub">CHANGING<br>ROOM ONLY</div>
        <div class="pill pill--note">NO MALE DAIRY<br>OPERATIVES</div>
        <div class="brand"><span class="brand-mark"></span>MARLOW DALE</div>
      </div>
    </div></div>
  </section>

  <section class="notice notice--mono" style="left:1520px;top:245px">
    <div class="frame"><div class="panel">
      <header class="panel-head"><div class="head-main">ATTENTION</div><div class="head-sub">PLEASE!</div></header>
      <div class="panel-body" style="padding-top:28px">
        <div class="title accent">FEMALE<br>VISITORS</div>
        <div class="title-sub">CHANGING<br>ROOM ONLY</div>
        <div class="pill pill--note">NO MALE DAIRY<br>OPERATIVES</div>
        <div class="brand">BRENWICK FOODS</div>
      </div>
    </div></div>
  </section>

  <!-- Row 2 -->
  <section class="notice" style="left:155px;top:884px">
    <div class="frame"><div class="panel">
      <header class="panel-head"><div class="head-main">ATTENTION</div><div class="head-sub">PLEASE!</div></header>
      <div class="panel-body" style="padding-top:40px">
        <div class="title accent">BLOCK FORMER<br>ROOM</div>
        <ul class="kit">
          <li class="pill">1 X DUST PAN</li>
          <li class="pill">1 X BRUSH</li>
          <li class="pill">1 X LONG HANDLE BRUSH</li>
          <li class="pill">1 X SQUEEGEE</li>
        </ul>
        <div class="brand"><span class="brand-mark"></span>MARLOW DALE</div>
      </div>
    </div></div>
  </section>

  <section class="notice notice--mono" style="left:610px;top:884px">
    <div class="frame"><div class="panel">
      <header class="panel-head"><div class="head-main">ATTENTION</div><div class="head-sub">PLEASE!</div></header>
      <div class="panel-body" style="padding-top:40px">
        <div class="title accent">BLOCK FORMER<br>ROOM</div>
        <ul class="kit">
          <li class="pill">1 X DUST PAN</li>
          <li class="pill">1 X BRUSH</li>
          <li class="pill">1 X LONG HANDLE BRUSH</li>
          <li class="pill">1 X SQUEEGEE</li>
        </ul>
        <div class="brand">BRENWICK FOODS</div>
      </div>
    </div></div>
  </section>

  <section class="notice" style="left:1065px;top:884px">
    <div class="frame"><div class="panel">
      <header class="panel-head"><div class="head-main">ATTENTION</div><div class="head-sub">PLEASE!</div></header>
      <div class="panel-body" style="padding-top:16px">
        <p class="copy">This wall comprises of a<br><strong class="accent">COMPOSITE PANEL</strong><br>and may contain flammable<br>core material.</p>
        <p class="copy">It must not be penetrated to<br>expose the insulation core<br>without a valid permit to work<br>document.</p>
        <p class="copy">Failure to observe this<br>precaution is considered a<br><strong class="accent">RED CARD</strong> offence.</p>
        <div class="pill pill--credit">Principle Designer &nbsp;- Daniel Pryce</div>
        <div class="brand"><span class="brand-mark"></span>MARLOW DALE</div>
      </div>
    </div></div>
  </section>

  <section class="notice notice--mono" style="left:1520px;top:884px">
    <div class="frame"><div class="panel">
      <header class="panel-head"><div class="head-main">ATTENTION</div><div class="head-sub">PLEASE!</div></header>
      <div class="panel-body" style="padding-top:16px">
        <p class="copy">This wall comprises of a<br><strong class="accent">COMPOSITE PANEL</strong><br>and may contain flammable<br>core material.</p>
        <p class="copy">It must not be penetrated to<br>expose the insulation core<br>without a valid permit to work<br>document.</p>
        <p class="copy">Failure to observe this<br>precaution is considered a<br><strong class="accent">RED CARD</strong> offence.</p>
        <div class="pill pill--credit">Principle Designer &nbsp;- Daniel Pryce</div>
        <div class="brand">BRENWICK FOODS</div>
      </div>
    </div></div>
  </section>

</div>
</body>
</html>
```